New Business Card Design for Manufacturing

We are an engineering/manufacturing company that offers Advanced machining/assembly/engineering services, as well as innovative products for the heavy duty engine cooling markets.

We are looking to get a new business card designed that is clean and modern looking, but still fits the wide range of technical/skilled work we do.

- We hope to use this design as the base for other design work in new Presentations, web, and print work.

Industry/Entity Type

Engineering

Contact Information for Business Card

Our preferred color of blue is (RGB) 22/71/159 but can vary slightly from that color. Our content will be our Logo and full company name (Corvath Tooling Works, Inc.), company address, name, job title, phone number with extension, cell number, fax number, website, and email address on the cards.
We'd like the full company name next to the logo, but we are open to other interpretations of that layout.
Preferably, we would like the back side to be clean with just our logo, and the front to contain all of the contact information.

Colors
2f74b4
0355a3
85abd2

Requirements
Must have
• - Logo, company name, needed content - We are open to interpretation beyond that.
• - Standard size business card.
• - Horizontal orientation.
• - Enough space for lengthy names / job titles (for example, a job title could read "Directory of Human Resources" or "V.P. of Governmental Affairs"). We need this to look clean, whether the title be short (CEO) or long (as described above).

```html
<!DOCTYPE html>
<html lang="en">
<head>
<meta charset="utf-8">
<title>Corvath Tooling Works – Business Card</title>
<link rel="stylesheet" href="https://fonts.googleapis.com/css2?family=Montserrat:wght@400;600;800&display=swap">
<style>
  :root {
    --brand-blue: #16479f;
    --brand-mid: #2f74b4;
    --brand-deep: #0355a3;
    --brand-light: #85abd2;
    --paper: #ffffff;
    --ink-grey: #6d6f73;
    --stage: #e9ebee;
  }
  * { margin: 0; padding: 0; box-sizing: border-box; }
  html, body { width: 1200px; height: 900px; overflow: hidden; }
  body {
    background: var(--stage);
    font-family: "Montserrat", sans-serif;
    position: relative;
  }
  .card {
    position: absolute;
    left: 250px;
    width: 700px;
    height: 400px;
    overflow: hidden;
    box-shadow: 0 6px 18px rgba(0,0,0,0.18);
  }
  /* Back side */
  .card-back {
    top: 35px;
    background: linear-gradient(45deg, var(--brand-deep) 0%, var(--brand-mid) 55%, var(--brand-light) 100%);
  }
  .card-back .base-band { position: absolute; left: 0; top: 0; width: 700px; height: 400px; }
  .back-brand {
    position: absolute;
    left: 40px;
    top: 222px;
    display: flex;
    align-items: flex-start;
    gap: 22px;
  }
  .wordmark {
    color: var(--paper);
    font-weight: 800;
    font-size: 52px;
    letter-spacing: 1px;
    line-height: 1;
    white-space: nowrap;
  }
  .tagline {
    color: var(--brand-light);
    font-weight: 600;
    font-size: 12px;
    letter-spacing: 1px;
    margin-top: 6px;
    white-space: nowrap;
  }
  .company-name {
    color: var(--paper);
    font-weight: 800;
    font-size: 17px;
    line-height: 1.05;
    text-transform: uppercase;
    margin-top: 2px;
  }
  .company-name small { font-size: 8px; font-weight: 600; }

  /* Front side */
  .card-front { top: 465px; background: var(--paper); }
  .logo-block {
    position: absolute;
    left: 50px;
    top: 0;
    width: 250px;
    height: 165px;
    background: var(--brand-blue);
    display: flex;
    flex-direction: column;
    justify-content: center;
    padding-left: 28px;
  }
  .logo-block .wordmark { font-size: 34px; }
  .logo-block .tagline { color: var(--paper); font-size: 10px; }
  .rule-long {
    position: absolute;
    left: 300px;
    top: 150px;
    width: 400px;
    height: 3px;
    background: var(--brand-blue);
  }
  .person { position: absolute; left: 58px; top: 190px; }
  .person-name {
    color: var(--brand-blue);
    font-weight: 800;
    font-size: 19px;
    letter-spacing: 0.5px;
  }
  .person-title { color: var(--ink-grey); font-size: 14px; margin-top: 2px; }
  .rule-short {
    position: absolute;
    left: 58px;
    top: 262px;
    width: 230px;
    height: 3px;
    background: var(--brand-light);
  }
  .contact-list { position: absolute; left: 58px; top: 278px; list-style: none; }
  .contact-list li {
    display: flex;
    align-items: center;
    gap: 12px;
    color: var(--ink-grey);
    font-size: 15px;
    height: 24px;
  }
  .contact-list svg { width: 17px; height: 17px; flex: none; }
  .address {
    position: absolute;
    right: 40px;
    top: 196px;
    color: var(--ink-grey);
    font-size: 14px;
  }
</style>
</head>
<body>

<section class="card card-back" aria-label="Card back">
  <svg class="base-band" viewBox="0 0 700 400" aria-hidden="true">
    <rect x="0" y="368" width="700" height="32" fill="#ffffff"/>
    <polygon points="0,352 390,352 400,316 700,316 700,368 0,368" fill="var(--brand-deep)"/>
    <polyline points="385,344 396,308 700,308" fill="none" stroke="#ffffff" stroke-width="2"/>
  </svg>
  <div class="back-brand">
    <div>
      <div class="wordmark">CORVATH</div>
      <div class="tagline">BUILT TO PERFORM</div>
    </div>
    <div class="company-name">Corvath<br>Tooling<br>Works <small>INC</small></div>
  </div>
</section>

<section class="card card-front" aria-label="Card front">
  <div class="logo-block">
    <div class="wordmark">CORVATH</div>
    <div class="tagline">BUILT TO PERFORM</div>
  </div>
  <div class="rule-long"></div>

  <div class="person">
    <div class="person-name">MARTIN HALE</div>
    <div class="person-title">V.P. of Governmental Affairs</div>
  </div>
  <div class="rule-short"></div>

  <ul class="contact-list">
    <li>
      <svg viewBox="0 0 20 20" aria-label="Phone"><circle cx="10" cy="10" r="9" fill="none" stroke="var(--brand-blue)" stroke-width="1.6"/><path d="M7 5.5l1.6 2.4-1 1.2a6 6 0 0 0 3.3 3.3l1.2-1 2.4 1.6-.8 1.6c-3.8-.3-7.2-3.7-7.5-7.5z" fill="var(--brand-blue)"/></svg>
      (864) 555-0142 x123
    </li>
    <li>
      <svg viewBox="0 0 20 20" aria-label="Mobile"><circle cx="10" cy="10" r="9" fill="none" stroke="var(--brand-blue)" stroke-width="1.6"/><rect x="7" y="4.5" width="6" height="11" rx="1.2" fill="none" stroke="var(--brand-blue)" stroke-width="1.4"/></svg>
      540-555-0183
    </li>
    <li>
      <svg viewBox="0 0 20 20" aria-label="Fax"><circle cx="10" cy="10" r="9" fill="none" stroke="var(--brand-blue)" stroke-width="1.6"/><rect x="5.5" y="8" width="9" height="5.5" fill="var(--brand-blue)"/><rect x="7" y="5" width="6" height="3" fill="none" stroke="var(--brand-blue)" stroke-width="1.2"/></svg>
      540-555-0147
    </li>
    <li>
      <svg viewBox="0 0 20 20" aria-label="Email"><circle cx="10" cy="10" r="9" fill="none" stroke="var(--brand-blue)" stroke-width="1.6"/><rect x="5.5" y="6.5" width="9" height="7" fill="none" stroke="var(--brand-blue)" stroke-width="1.3"/><path d="M5.5 6.5l4.5 4 4.5-4" fill="none" stroke="var(--brand-blue)" stroke-width="1.3"/></svg>
      martin@corvath.com
    </li>
  </ul>

  <div class="address">418 Ridgeline Rd , Harlow KY 42071</div>
</section>

</body>
</html>
```